Hadley's Groundwork Crew needs a logo/business cards.

i've just started a new Labouring Business, Called Hadley's Groundwork Crew, I provide high quality labouring servicing to local Builders and Tradesmen.
I'd like my business cards to reflect the hard work and dedication I put into my business.
I'd like to see Burnt Orange and blacks in the cards and logo.
I want my cards to catch peoples eye as there is A lot of dull business cards in my industry.

Target Market(s)

Builders and other tradesmen

Contact Information for Business Card

Hadley's Groundwork Crew

Font styles to use
Sans Serif

Colors
f78f20
ffc214
000000
ffffff

Requirements
Must have
• My name : Tom Hadley
• My Number: 0457962381
• Email Address : hadleygroundworkcrew@mailbarn.net
• A Sharp and Professional Design
Nice to have
• A unique design that separates my Cards from others,
• As I try to provide unique service to my clients I'd love my cards/logo to reflect this.

```html
<!DOCTYPE html>
<html lang="en">
<head>
<meta charset="utf-8">
<title>Hadley's Groundwork Crew — Business Cards</title>
<link rel="stylesheet" href="https://fonts.googleapis.com/css2?family=Lato:wght@400;700&family=Montserrat:wght@500&display=swap">
<style>
  :root {
    --burnt-orange: #f78f20;
    --card-black: #1d1d1d;
    --white: #ffffff;
    --backdrop: #ebe8e3;
    --card-shadow: rgba(0, 0, 0, 0.28);
  }
  html, body {
    margin: 0;
    padding: 0;
    overflow: hidden;
  }
  .canvas {
    position: relative;
    width: 1200px;
    height: 900px;
    background: var(--backdrop);
    overflow: hidden;
  }
  .card {
    position: absolute;
    box-shadow: 3px 4px 8px var(--card-shadow);
  }
  .card--front {
    left: 330px;
    top: 90px;
    width: 555px;
    height: 343px;
    background: var(--burnt-orange);
    color: var(--white);
    font-family: "Lato", sans-serif;
    text-align: center;
  }
  .holder-name {
    position: absolute;
    left: 0;
    right: 0;
    top: 116px;
    margin: 0;
    font-size: 26px;
    font-weight: 700;
    letter-spacing: 0.2px;
  }
  .name-rule {
    position: absolute;
    left: 206px;
    top: 166px;
    width: 144px;
    height: 1.5px;
    background: var(--white);
  }
  .contact {
    position: absolute;
    left: 0;
    right: 0;
    top: 190px;
    margin: 0;
    font-size: 20px;
    font-weight: 400;
    line-height: 27px;
  }
  .card--back {
    left: 330px;
    top: 470px;
    width: 560px;
    height: 342px;
    background: var(--card-black);
  }
  .brand-disc {
    position: absolute;
    left: 218px;
    top: 82px;
    width: 118px;
    height: 118px;
    border-radius: 50%;
    background: var(--burnt-orange);
  }
  .brand-name {
    position: absolute;
    left: 0;
    right: 0;
    top: 208px;
    margin: 0;
    font-family: "Montserrat", sans-serif;
    font-weight: 500;
    color: var(--burnt-orange);
    text-align: center;
    text-transform: uppercase;
  }
  .brand-name__main {
    display: block;
    font-size: 34px;
    line-height: 40px;
    letter-spacing: 0.5px;
  }
  .brand-name__sub {
    display: block;
    font-size: 13px;
    line-height: 16px;
    letter-spacing: 3px;
  }
</style>
</head>
<body>
  <main class="canvas">
    <section class="card card--front" aria-label="Business card front">
      <h1 class="holder-name">TOM HADLEY</h1>
      <div class="name-rule"></div>
      <p class="contact">
        0457962381<br>
        hadleygroundworkcrew@mailbarn.net
      </p>
    </section>

    <section class="card card--back" aria-label="Business card back">
      <div class="brand-disc"></div>
      <p class="brand-name">
        <span class="brand-name__main">Hadley's</span>
        <span class="brand-name__sub">Groundwork Crew</span>
      </p>
    </section>
  </main>
</body>
</html>
```